Business card design needed

Company Name: Helmfield Advisory

We work with boards and businesses to enhance their governance structures, board room performance
Based on the Gold Coast Australia

Industry/Entity Type

Business

Contact Information for Business Card

Marla Venning
PO Box 628
Coral Shores Qld 4236

marla@helmfieldadvisory.com.au
0427 691835

Requirements
Nice to have
• I quite like "cogs" but am open to suggestions

```html
<!DOCTYPE html>
<html lang="en">
<head>
<meta charset="utf-8">
<title>Helmfield Advisory – Business Card</title>
<link rel="stylesheet" href="https://fonts.googleapis.com/css2?family=Michroma&display=swap">
<style>
  :root {
    --page-bg: #ffffff;
    --card-bg: #ffffff;
    --card-edge: #d9d9d9;
    --ink: #111111;
    --mark-blue: #3d4fd6;
  }
  * { margin: 0; padding: 0; box-sizing: border-box; }
  html, body {
    width: 1200px;
    height: 1000px;
    overflow: hidden;
    background: var(--page-bg);
  }
  .canvas {
    position: relative;
    width: 1200px;
    height: 1000px;
  }
  .business-card {
    position: absolute;
    left: 219px;
    top: 263px;
    width: 764px;
    height: 437px;
    background: var(--card-bg);
    border: 3px solid var(--card-edge);
    font-family: "Michroma", sans-serif;
    color: var(--ink);
    text-align: center;
  }
  .brand-mark {
    position: absolute;
    left: 50%;
    top: 78px;
    width: 76px;
    height: 76px;
    margin-left: -38px;
    display: block;
  }
  .company-name {
    position: absolute;
    left: 0;
    right: 0;
    top: 186px;
    font-size: 36px;
    font-weight: 400;
    letter-spacing: 4px;
    white-space: nowrap;
    text-transform: uppercase;
  }
  .person-name {
    position: absolute;
    left: 0;
    right: 0;
    top: 274px;
    font-size: 20px;
    font-weight: 400;
    font-variant: small-caps;
    letter-spacing: 4.5px;
    white-space: nowrap;
  }
  .contact-details {
    position: absolute;
    left: 0;
    right: 0;
    top: 360px;
    font-size: 14.5px;
    font-style: normal;
    font-variant: small-caps;
    letter-spacing: 5.5px;
    line-height: 24px;
    white-space: nowrap;
  }
  .contact-details p { margin: 0; }
</style>
</head>
<body>
  <main class="canvas">
    <section class="business-card">
      <svg class="brand-mark" viewBox="0 0 76 76" aria-hidden="true">
        <circle cx="38" cy="38" r="38" fill="var(--mark-blue)"/>
      </svg>
      <h1 class="company-name">Helmfield Advisory</h1>
      <p class="person-name">Marla Venning</p>
      <address class="contact-details">
        <p>PO Box 628 Coral Shores Qld 4236</p>
        <p>marla@helmfieldadvisory.com.au 0427 691835</p>
      </address>
    </section>
  </main>
</body>
</html>
```